V.Crest Gin - Bottle label Design

We are manufacturers of Gin in South Africa.
The name of our Gin is V.Crest Gin with Q standing for Vukhamba, a Xhosa Village in the region of Eastern Cape.

We would like our brand to depict the following (really the focus of Gold on it)
> Prosperity of the place
> Wealth of the place, land, material or in the people
> Gold rush, potential, hope

As the brand matures, we would like to have campaigns with it. See ideas below:
> V.Crest Premium
> Red dusk edition
Limited edition will be released every year
- V.Crest entabeni (location)
- V.Crest elwandle (location)

> Each batch of bottles with focus on a specific area/location in Vukhamba. One that is known and will be highlighted on the map design of the bottle.
Bottles based on landmarks in Vukhamba and landmark design in the Big V.

Below we tried but we are not where we really want to be in terms of Gin Bottle elegance.

Target Market(s)

Target market is the young crowd. Young Xhosa men and women working really hard to get their goals. Positive thinkers. Elegant. Fresh. Bold. Age from 24 to 45. People who enjoy quality products.

Industry/Entity Type

Beverage Industry. Craft Gin.

Font styles to use
Sans Serif
Decorative

Colors
FFF300
FFF600
FEFA6F
FFFEC7
FFFEE8
FFC000
F8CF3A
FAE287
FDF2CF
FEFAEE

Requirements
Must have
• Gold colour as a theme. Try and make the background textured.

```html
<!DOCTYPE html>
<html lang="en">
<head>
<meta charset="utf-8">
<title>V.Crest Gin — Bottle Label</title>
<link rel="stylesheet" href="https://fonts.googleapis.com/css2?family=Archivo+Black&family=Cinzel:wght@500&family=Michroma&family=Oswald:wght@500&display=swap">
<style>
  :root {
    --backdrop: #fea629;
    --paper: #f4f1ee;
    --paper-shade: #ebe6e1;
    --ink: #111111;
    --ink-soft: #4a4540;
    --rule: #b9b2aa;
    --gold-dark: #6e4514;
    --gold-mid: #c08a3e;
    --gold-light: #fbe39a;
    --gold-pale: #fffee8;
    --hill-amber: #f4a93a;
    --hill-sand: #f1b257;
    --hill-rust: #cd743b;
    --hill-coral: #ec967a;
  }

  * { box-sizing: border-box; margin: 0; padding: 0; }

  html, body {
    width: 1200px;
    height: 849px;
    overflow: hidden;
    background: var(--backdrop);
  }

  .canvas {
    position: relative;
    width: 1200px;
    height: 849px;
  }

  .label {
    position: absolute;
    left: 220px;
    top: 86px;
    width: 760px;
    height: 677px;
    background:
      radial-gradient(ellipse 40% 30% at 20% 40%, rgba(0,0,0,0.025), transparent 70%),
      radial-gradient(ellipse 35% 25% at 75% 70%, rgba(0,0,0,0.03), transparent 70%),
      radial-gradient(ellipse 30% 20% at 60% 20%, rgba(0,0,0,0.02), transparent 70%),
      linear-gradient(180deg, var(--paper), var(--paper-shade));
    overflow: hidden;
  }

  .landscape {
    position: absolute;
    left: 0;
    top: 37px;
    width: 760px;
    height: 170px;
    background: linear-gradient(180deg,
      var(--hill-amber) 0%,
      var(--hill-sand) 40%,
      var(--hill-rust) 70%,
      var(--hill-coral) 100%);
    border-radius: 40% 60% 30% 20% / 30% 25% 20% 25%;
  }

  .brand-name {
    position: absolute;
    left: 0;
    width: 100%;
    top: 238px;
    text-align: center;
    font-family: "Archivo Black", sans-serif;
    font-size: 112px;
    line-height: 1;
    letter-spacing: 1px;
    color: var(--ink);
  }

  .origin {
    position: absolute;
    left: 0;
    width: 100%;
    top: 389px;
    text-align: center;
    font-family: "Michroma", sans-serif;
    font-size: 13px;
    letter-spacing: 6px;
    color: var(--ink-soft);
  }

  .hairline {
    position: absolute;
    left: 97px;
    width: 566px;
    height: 0;
    border-top: 1px dotted var(--rule);
  }
  .hairline.top { top: 420px; }
  .hairline.r1 { top: 494px; }
  .hairline.r2 { top: 523px; }
  .hairline.r3 { top: 567px; }

  .product {
    position: absolute;
    left: 0;
    width: 100%;
    top: 418px;
    display: flex;
    justify-content: center;
    align-items: center;
    gap: 26px;
  }

  .product-name {
    font-family: "Archivo Black", sans-serif;
    font-size: 64px;
    line-height: 1;
    color: var(--ink);
  }

  .dash-pair {
    width: 62px;
    height: 10px;
    border-top: 2px solid var(--gold-mid);
    border-bottom: 2px solid var(--gold-mid);
  }

  .facts {
    position: absolute;
    left: 97px;
    top: 494px;
    width: 566px;
    height: 73px;
    display: grid;
    grid-template-columns: 213px 1fr;
    grid-template-rows: 29px 44px;
  }
  .facts > div {
    display: flex;
    align-items: center;
    padding-left: 10px;
    color: var(--ink);
  }
  .facts .left { border-right: 1px dotted var(--rule); }
  .facts .region {
    font-family: "Cinzel", serif;
    font-size: 16px;
    letter-spacing: 1.5px;
    color: var(--ink-soft);
  }
  .facts .quality {
    font-family: "Michroma", sans-serif;
    font-size: 11px;
    letter-spacing: 2.5px;
    padding-left: 22px;
    color: var(--ink-soft);
  }
  .facts .volume, .facts .taste {
    font-family: "Oswald", sans-serif;
    font-size: 17px;
    letter-spacing: 4px;
  }
  .facts .taste { padding-left: 22px; letter-spacing: 5px; }

  .gold-ribbon {
    position: absolute;
    left: 95px;
    top: 588px;
    width: 570px;
    height: 20px;
    border-radius: 10px;
    background: linear-gradient(90deg, var(--gold-dark) 0%, var(--gold-mid) 20%, var(--gold-light) 45%, var(--gold-pale) 55%, var(--gold-mid) 80%, var(--gold-light) 95%, var(--gold-mid) 100%);
    display: flex;
    align-items: center;
    justify-content: center;
    font-family: "Michroma", sans-serif;
    font-size: 13px;
    letter-spacing: 10px;
    color: var(--ink);
  }

  .gold-base {
    position: absolute;
    left: 4px;
    right: 0;
    bottom: 0;
    height: 20px;
    background: linear-gradient(90deg, var(--gold-dark) 0%, var(--gold-mid) 25%, var(--gold-pale) 38%, var(--gold-mid) 55%, var(--gold-light) 75%, var(--gold-mid) 88%, var(--gold-light) 100%);
  }
</style>
</head>
<body>
<main class="canvas">
  <section class="label">
    <div class="landscape" role="img" aria-label="Illustrated landscape of rolling golden hills with acacia trees and small village houses"></div>

    <h1 class="brand-name">V.Crest</h1>
    <p class="origin">•MADE IN SOUTH AFRICA•</p>

    <div class="hairline top"></div>

    <div class="product">
      <span class="dash-pair"></span>
      <h2 class="product-name">GIN</h2>
      <span class="dash-pair"></span>
    </div>

    <div class="hairline r1"></div>
    <div class="hairline r2"></div>
    <div class="hairline r3"></div>

    <div class="facts">
      <div class="left region">VUKHAMBA REGION</div>
      <div class="quality">TRIPPLE DISTILLED QUALITY</div>
      <div class="left volume">37.5% ALC&nbsp;|&nbsp;750ML</div>
      <div class="taste">A RICH &amp; AROMATIC TASTE</div>
    </div>

    <div class="gold-ribbon">•MADE IN THE EASTERN CAPE•</div>
    <div class="gold-base"></div>
  </section>
</main>
</body>
</html>
```